Traineeport.Asia, a social enterprise in Asia, needs a website!

I need a website designed for Traineeport.Asia, which is a social enterprise in Asia that connects potential interns with internship opportunities in the region.

Please read the attached wireframe and submit a homepage designs with text, based on the attached wireframe, from which we will choose and select the best design. Please note that we only want website designs; functionality, coding and programming are not required

The designer that provides the best designed home page, will then design all other pages of the website, and will receive the fee. We have already come up with one design (see wireframe in the attached doc) that designers may review for ideas.

Target Market(s)

University and graduate students in Asia.

Industry/Entity Type

Social

Number of Pages Required

5+ page

Font styles to use
Sans Serif

Requirements
Must have
• I want a website that doesn't require a significant amount of scrolling, and is well-designed so that it is easy to understand the website's purpose, how to navigate around the website, and utilize it.
Nice to have
• Easy to see all elements of the website without scrolling.

```html
<!DOCTYPE html>
<html lang="en">
<head>
<meta charset="utf-8">
<title>Traineeport.Asia — Home</title>
<link href="https://fonts.googleapis.com/css2?family=Raleway:wght@400;500;600&family=Open+Sans:wght@400;600&display=swap" rel="stylesheet">
<style>
:root{
  --green:#5eb32a;
  --green-dark:#4a9a1c;
  --green-light:#6fc035;
  --blue:#1f45a6;
  --navy:#1a3f8f;
  --text:#444;
  --muted:#666;
  --panel:#dcdcdc;
  --panel-line:#c6c6c6;
  --white:#fff;
}
*{box-sizing:border-box;margin:0;padding:0}
html,body{width:1061px;height:1200px;overflow:hidden;background:var(--white)}
body{position:relative;font-family:'Open Sans',sans-serif;color:var(--text)}
a{text-decoration:none}
.abs{position:absolute}
.header{left:0;top:0;width:1061px;height:93px;background:linear-gradient(#fff,#ececec)}
.brand{left:172px;top:46px;display:flex;align-items:center;gap:8px;font-family:'Raleway',sans-serif;font-weight:600;font-size:20px;color:var(--navy)}
.brand-dot{width:12px;height:12px;border-radius:50%;background:var(--green)}
.social-top{left:800px;top:60px;display:flex;gap:9px}
.social-top span{width:16px;height:16px;border-radius:50%;background:var(--navy)}
.social-top span:nth-child(1){background:#3aa0d8}
.social-top span:nth-child(4){background:#d33c2e}
.nav{left:0;top:93px;width:1061px;height:42px;background:linear-gradient(var(--green-light),var(--green-dark));display:flex;padding-left:170px}
.nav a{font-family:'Raleway',sans-serif;font-size:13.5px;color:var(--white);line-height:42px;padding:0 18px 0 27px;border-right:1px solid rgba(0,0,0,.15)}
.nav a:last-child{border:none}
.hero{left:170px;top:146px;width:720px;height:262px;background:linear-gradient(100deg,#8a7a5a 0%,#c8b98e 40%,#e2d7b5 60%,#b8a774 100%)}
.hero-caption{left:169px;top:312px;width:284px;height:96px;background:rgba(31,69,166,.93);color:var(--white);font-family:'Raleway',sans-serif;font-weight:500;font-size:15px;line-height:18.5px;padding:20px 10px 0 18px}
.hero-arrows{left:856px;top:381px;width:34px;height:27px;background:var(--green)}
.col-title{font-family:'Raleway',sans-serif;font-weight:500;font-size:17px;line-height:21px}
.col-title small{display:block;font-size:15px}
.col-text{font-size:8.3px;line-height:13px;color:var(--text);margin-top:10px;width:240px}
.btn{display:inline-block;color:var(--white);font-family:'Raleway',sans-serif;font-weight:500;font-size:12px;text-align:center}
.intro-students{left:169px;top:436px}
.intro-students .col-title{color:var(--navy)}
.intro-employers{left:447px;top:436px}
.intro-employers .col-title{color:var(--green)}
.intro-students .btn{background:var(--blue);width:111px;height:29px;line-height:29px;margin-top:7px;margin-left:3px}
.intro-employers .btn{background:var(--green);width:111px;height:29px;line-height:29px;margin-top:7px}
.divider{left:422px;top:437px;width:1px;height:148px;background:#ccc}
.section-title{font-family:'Raleway',sans-serif;font-weight:500;font-size:17px}
.featured-title{left:169px;top:582px;color:var(--navy)}
.job{display:flex;gap:7px;position:absolute;width:260px}
.job svg{width:22px;height:22px;fill:var(--green);flex:none;margin-top:3px}
.job b{display:block;font-weight:400;font-size:11px;color:#444}
.job i{display:block;font-style:normal;font-size:9.5px;color:var(--muted);margin-top:2px}
.view-more{left:168px;top:765px;width:66px;height:21px;line-height:21px;font-size:9px;background:var(--blue)}
.resources-title{left:169px;top:822px;color:var(--green)}
.res-photo{left:170px;top:854px;width:95px;height:70px;background:linear-gradient(#6c6a62,#2a2a2a)}
.res-body{left:275px;top:852px;width:380px}
.res-body h3{font-weight:600;font-size:11px;color:#444}
.res-body p{font-size:7.6px;line-height:14px;color:var(--muted);margin-top:3px}
.res-body a{font-weight:600;font-size:10px;color:var(--navy)}
.social-box{left:693px;top:420px;width:197px;height:78px;background:var(--green);text-align:center;color:var(--white)}
.social-box h2{font-family:'Raleway',sans-serif;font-weight:500;font-size:15px;margin-top:12px}
.social-box .dots{display:flex;justify-content:center;gap:15px;margin-top:10px}
.social-box .dots span{width:21px;height:21px;border-radius:50%;background:#314d9b}
.social-box .dots span:nth-child(2){background:#37a9e3}
.social-box .dots span:nth-child(3){background:#dc4a38}
.social-box .dots span:nth-child(4){background:#1a7ac0}
.feed{left:693px;top:509px;width:196px;height:433px;background:var(--panel)}
.feed-head{height:34px;display:flex;align-items:center;gap:6px;padding-left:10px;font-weight:600;font-size:11px;color:#333;background:linear-gradient(#eee,#dedede);border-bottom:1px solid var(--panel-line)}
.feed-head span{width:14px;height:14px;border-radius:50%;background:#3aa0d8}
.post{display:flex;gap:7px;padding:8px 8px 0 6px;border-bottom:1px solid var(--panel-line)}
.post .av{width:26px;height:26px;background:#f4f4f4;flex:none;margin-top:2px}
.post p{font-size:6.3px;line-height:9.5px;color:#333}
.post p b{font-weight:400;color:#2a7fc6}
.post p em{display:block;font-style:normal;color:#777;margin-top:1px}
.footer{left:0;top:972px;width:1061px;height:184px;background:linear-gradient(var(--green-light),var(--green))}
.footer-col{position:absolute;top:32px;color:var(--white)}
.footer-col h4{font-family:'Raleway',sans-serif;font-weight:500;font-size:16px;margin-bottom:6px}
.footer-col a{display:block;font-family:'Raleway',sans-serif;font-size:11px;color:var(--white);line-height:18px}
.fsep{position:absolute;top:36px;width:1px;height:113px;background:rgba(255,255,255,.35)}
.f-social{display:flex;gap:10px;margin-top:6px}
.f-social span{width:15px;height:15px;border-radius:50%;background:var(--white)}
.f-brand{position:absolute;left:752px;top:87px;display:flex;align-items:center;gap:7px;font-family:'Raleway',sans-serif;font-weight:600;font-size:17px;color:var(--white)}
.f-brand i{width:11px;height:11px;border-radius:50%;background:var(--white)}
.copy{left:0;top:1156px;width:1061px;height:44px;background:var(--green-dark);font-size:8.5px;color:#d9eecb;padding:18px 0 0 173px}
</style>
</head>
<body>
<header class="header abs">
  <div class="brand abs"><span class="brand-dot"></span>Traineeport.Asia</div>
  <div class="social-top abs"><span></span><span></span><span></span><span></span></div>
</header>
<nav class="nav abs">
  <a href="#">About Us</a><a href="#">Search Internships</a><a href="#">Post an Internship</a><a href="#">Login</a><a href="#">Registration</a>
</nav>

<div class="hero abs" role="img" aria-label="Photo of a smiling student in a yellow polo shirt in a university hallway"></div>
<div class="hero-caption abs">Want to get professional experience while still in college/university or graduate school</div>
<div class="hero-arrows abs"><svg width="34" height="27" viewBox="0 0 34 27"><path d="M14 8l-5 5.5 5 5.5M20 8l5 5.5-5 5.5" fill="none" stroke="#fff" stroke-width="1.6"/></svg></div>

<section class="intro-students abs">
  <h2 class="col-title">Want Professional Experience<small>while still in College/ University</small></h2>
  <p class="col-text">Class aptent taciti sociosqu ad litora torquent per conubia nostra per inceptos hymenaeos Proin nulla arcu</p>
  <a class="btn" href="#">For Students</a>
</section>
<div class="divider abs"></div>
<section class="intro-employers abs">
  <h2 class="col-title">Get in connection with<br>highly educated students</h2>
  <p class="col-text">Class aptent taciti sociosqu ad litora torquent per conubia nostra per inceptos hymenaeos Proin nulla arcu</p>
  <a class="btn" href="#">For Employers</a>
</section>

<h2 class="section-title featured-title abs">Featured Internships</h2>
<div class="job" style="left:170px;top:624px"><svg viewBox="0 0 24 24"><path d="M21 5a5 5 0 0 1-6.5 5L5 19.5 3.5 18 13 8.5A5 5 0 0 1 19 2l-3 3 1 2 2 1z"/></svg><div><b>Operation Intern</b><i>Kestrel WirelessClinton, Shenzen</i></div></div>
<div class="job" style="left:450px;top:624px"><svg viewBox="0 0 24 24"><path d="M4 5h16v11H4zm2 2v7h12V7zM1 18h22v2H1z"/></svg><div><b>IT Developer</b><i>Kestrel WirelessClinton, Shenzen</i></div></div>
<div class="job" style="left:170px;top:668px"><svg viewBox="0 0 24 24"><circle cx="12" cy="6" r="4"/><path d="M3 23v-5a6 6 0 0 1 6-6h6a6 6 0 0 1 6 6v5z"/></svg><div><b>Engineering Intern</b><i>Lumora Cable Communication, Beijing</i></div></div>
<div class="job" style="left:450px;top:668px"><svg viewBox="0 0 24 24"><path d="M9 3h6v3h7v14H2V6h7zm2 2v1h2V5zM2 11h20v2H2z"/></svg><div><b>Busieness Executive</b><i>Lumora Cable Communication, Beijing</i></div></div>
<div class="job" style="left:170px;top:710px"><svg viewBox="0 0 24 24"><path d="M10 3C5 3 1 6 1 10c0 2 1 4 3 5l-1 4 5-3h2c5 0 9-3 9-6s-4-7-9-7zm0 2c4 0 7 2 7 5s-3 5-7 5-7-2-7-5 3-5 7-5z"/></svg><div><b>Consultant Intern</b><i>Harbourline Bank, Shanghai</i></div></div>
<div class="job" style="left:450px;top:710px"><svg viewBox="0 0 24 24"><path d="M11 3a9 9 0 1 0 9 10h-9z"/><path d="M13 1v10h10A10 10 0 0 0 13 1z"/></svg><div><b>Analyzer</b><i>Harbourline Bank, Shanghai</i></div></div>
<a class="btn view-more abs" href="#">View More</a>

<h2 class="section-title resources-title abs">Resources</h2>
<div class="res-photo abs" role="img" aria-label="Photo of a graduate in cap and gown giving a thumbs up"></div>
<div class="res-body abs">
  <h3>Sample CV/Resume</h3>
  <p>Writing a résumé or CV is one of the first steps in a successful internship search strategy. Generally, it should be considered as a one-page selling tool and other than perhaps a face-to-face meeting or cover letter, your CV may be the first impression you make at a firm.</p>
  <a href="#">Read More</a>
</div>

<aside class="social-box abs"><h2>Social Media</h2><div class="dots"><span></span><span></span><span></span><span></span></div></aside>
<aside class="feed abs">
  <div class="feed-head"><span></span>Latest Posts Plugin</div>
  <div class="post" style="height:45px"><div class="av"></div><p><b>loomthemes</b> Check out Day 321 - Post post - <b>http://dailymock.com/day/321/</b><em>12 minutes ago</em></p></div>
  <div class="post" style="height:58px"><div class="av"></div><p><b>roan</b> Woohoo! Check out the Chirpline Search Plugin I just released with LoomThemes! <b>http://loomthem.es/chirp</b><em>45 minutes ago from &nbsp; Harbour Lookout</em></p></div>
  <div class="post" style="height:47px"><div class="av"></div><p><b>dailymock</b> Chirpline plus PagePress plus <b>@loomthemes</b> = win.<em>1 hour ago</em></p></div>
  <div class="post" style="height:50px"><div class="av"></div><p><b>benwaller</b> I love Rally Force so much I traded in my first-born for RF.<em>1 hour ago</em></p></div>
  <div class="post" style="height:48px"><div class="av"></div><p><b>benwaller</b> I love Rally Force so much I traded in my first-born for RF.<em>1 hour ago</em></p></div>
  <div class="post" style="height:49px"><div class="av"></div><p><b>benwaller</b> I love Rally Force so much I traded in my first-born for RF.<em>1 hour ago</em></p></div>
  <div class="post" style="height:48px"><div class="av"></div><p><b>benwaller</b> I love Rally Force so much I traded in my first-born for RF.<em>1 hour ago</em></p></div>
  <div class="post" style="height:50px;border:none"><div class="av"></div><p><b>benwaller</b> I love Rally Force so much I traded in my first-born for RF.<em>1 hour ago</em></p></div>
</aside>

<footer class="footer abs">
  <div class="footer-col" style="left:172px"><h4>Quick Links</h4><a href="#">Traineeport.Asia</a><a href="#">About Us</a><a href="#">Search for Internships</a><a href="#">Registration</a><a href="#">Post an Internship</a></div>
  <div class="fsep" style="left:310px"></div>
  <div class="footer-col" style="left:337px"><h4>Services</h4><a href="#">Overview</a><a href="#">Featured Internships</a><a href="#">Terms and Conditions</a><a href="#">Contact Us</a></div>
  <div class="fsep" style="left:471px"></div>
  <div class="footer-col" style="left:501px"><h4>Resources</h4><a href="#">Our Team</a><a href="#">Support</a><a href="#">Blogs</a><a href="#">Term of Use</a></div>
  <div class="fsep" style="left:606px"></div>
  <div class="footer-col" style="left:635px"><h4>Follow Us</h4><div class="f-social"><span></span><span></span><span></span><span></span></div></div>
  <div class="f-brand"><i></i>Traineeport.Asia</div>
</footer>
<div class="copy abs">© 2015 Company Name &nbsp;All right reserved</div>
</body>
</html>
```